New singe page website for our software development company

We need a single webpage that includes information about our company, contact details and a job posting. It should scroll vertically with some cool animations and parallax scrolling effects.

We are a software development consulting company that writes custom software for our customers. The webpage should have graphics and illustrations that illustrate this.

Find our logo attached, it can be modified as needed.

Thanks for all the design. When looking through the various design it's clear to us, that car related images does not look right.

We got to have software design/engineering images instead.

Our unique selling points are:

• Custom software development
• Project Managment
• Industry Services
We want these displayed with some text and icons. The icons should either have the red/brown colour from our logo, or a colour that matches the design

Software

```html
<!DOCTYPE html>
<html lang="en">
<head>
<meta charset="utf-8">
<title>Keelstone Consult — Software Development Consulting</title>
<link rel="stylesheet" href="https://fonts.googleapis.com/css2?family=Open+Sans:wght@400;600&family=Arimo:wght@400;700&display=swap">
<style>
  :root {
    --brand: #7a2410;
    --brand-deep: #6a1e0c;
    --ink: #333333;
    --muted: #666666;
    --link: #1a8fc9;
    --line: #c9c9c9;
    --button: #4a4a4a;
    --footer: #555555;
    --white: #ffffff;
  }
  * { box-sizing: border-box; margin: 0; padding: 0; }
  html, body { width: 695px; height: 1200px; overflow: hidden; background: var(--white); }
  body { position: relative; font-family: "Arimo", Arial, sans-serif; color: var(--ink); }
  .abs { position: absolute; }

  /* Header */
  .site-header { position: absolute; left: 0; top: 0; width: 695px; height: 70px; background: var(--white); }
  .brand-name { left: 50px; top: 12px; font-family: "Open Sans", sans-serif; font-weight: 600; font-size: 25px; color: var(--brand); line-height: 1; }
  .brand-tagline { left: 50px; top: 46px; font-family: "Open Sans", sans-serif; font-size: 10.5px; color: var(--brand); line-height: 1; }
  .main-nav a { position: absolute; top: 30px; height: 20px; line-height: 20px; font-family: "Open Sans", sans-serif; font-size: 10px; color: var(--ink); text-decoration: none; text-align: center; }
  .main-nav .is-active { background: var(--brand); color: var(--white); width: 42px; }

  /* Hero */
  .hero { position: absolute; left: 0; top: 70px; width: 695px; height: 278px; overflow: hidden; }
  .hero-backdrop { position: absolute; inset: 0; background: radial-gradient(ellipse at 30% 40%, #6b4a34 0%, #3c2a1f 45%, #1f1814 100%), #2a1f18; }
  .hero-backdrop::after { content: ""; position: absolute; inset: 0; background: linear-gradient(90deg, rgba(40,25,15,.2) 0%, rgba(0,0,0,0) 50%, rgba(40,70,90,.35) 100%); }
  .hero-arrow { position: absolute; top: 121px; width: 34px; height: 34px; border-radius: 50%; background: rgba(0,0,0,.28); }
  .hero-arrow svg { position: absolute; left: 11px; top: 10px; }
  .hero-title { left: 115px; top: 56px; font-family: "Open Sans", sans-serif; font-size: 19px; color: var(--white); line-height: 1; }
  .hero-points { list-style: none; }
  .hero-points li { position: absolute; left: 116px; font-family: "Open Sans", sans-serif; font-size: 10.5px; color: var(--white); line-height: 12px; padding-left: 20px; white-space: nowrap; }
  .hero-points li svg { position: absolute; left: 0; top: 0; }
  .hero-device { left: 386px; top: 40px; width: 157px; height: 204px; border-radius: 8px; background: #1b1b1b; border: 1px solid #6a6a6a; }
  .hero-device-screen { position: absolute; left: 15px; top: 15px; width: 126px; height: 172px; background: linear-gradient(160deg, #0a2a40 0%, #0f5f86 45%, #083049 100%); }

  /* Services */
  .intro-heading { left: 0; top: 382px; width: 695px; text-align: center; font-weight: 700; font-size: 16.5px; color: var(--brand); line-height: 1; }
  .intro-text { left: 52px; top: 416px; width: 592px; text-align: center; font-size: 8.7px; line-height: 13px; color: var(--muted); }
  .service { position: absolute; top: 469px; width: 170px; text-align: center; }
  .service-icon { display: block; margin: 0 auto; }
  .service-title { margin-top: 9px; font-size: 13px; color: var(--brand); line-height: 1; }
  .service-text { margin-top: 6px; font-size: 8.6px; line-height: 12.3px; color: var(--muted); letter-spacing: .3px; }

  /* Jobs and news */
  .column-heading { top: 630px; font-size: 17px; color: var(--brand); line-height: 1; }
  .jobs-subheading { left: 76px; top: 661px; font-size: 10.5px; color: var(--ink); line-height: 1; }
  .job { position: absolute; left: 77px; padding-left: 17px; }
  .job svg { position: absolute; left: 0; top: 0; }
  .job-title { font-size: 10px; color: var(--link); line-height: 11px; }
  .job-detail { margin-top: 5px; font-size: 8.6px; color: var(--ink); line-height: 10px; }
  .news-list { list-style: none; }
  .news-list li { position: absolute; left: 392px; width: 240px; padding-left: 9px; font-size: 8.5px; line-height: 15.3px; color: var(--ink); }
  .news-list li::before { content: "›"; position: absolute; left: 0; top: -1px; font-weight: 700; }

  /* Contact */
  .contact-heading { left: 0; top: 806px; width: 695px; text-align: center; font-size: 18px; color: var(--brand); line-height: 1; }
  .field-label { left: 80px; font-size: 8.5px; color: var(--ink); line-height: 1; }
  .field { position: absolute; left: 80px; width: 258px; border: 1px solid var(--line); background: var(--white); font-size: 8.5px; color: var(--ink); padding: 0 9px; }
  .field-input { height: 31px; line-height: 29px; }
  .field-message { height: 64px; padding-top: 10px; line-height: 1; }
  .send-button { left: 274px; top: 1067px; width: 64px; height: 27px; background: var(--button); color: var(--white); font-size: 11px; line-height: 27px; text-align: center; }
  .location-map { left: 396px; top: 854px; width: 233px; height: 94px; background: linear-gradient(135deg, #e6e1d6 0%, #ddd8cc 40%, #d7e0c9 70%, #e3ddd0 100%); }
  .contact-info { position: absolute; font-family: "Open Sans", sans-serif; font-size: 8.7px; line-height: 16.5px; color: var(--ink); }
  .contact-info svg { position: absolute; left: -16px; top: 3px; }

  /* Footer */
  .site-footer { position: absolute; left: 0; top: 1130px; width: 695px; height: 70px; background: var(--footer); }
  .footer-links { left: 51px; top: 22px; font-size: 8.4px; color: var(--white); line-height: 1; }
  .footer-copy { left: 51px; top: 43px; font-size: 8.4px; color: var(--white); line-height: 1; }
  .social { position: absolute; top: 25px; width: 22px; height: 22px; }
</style>
</head>
<body>

<header class="site-header">
  <div class="abs brand-name">Keelstone Consult</div>
  <div class="abs brand-tagline">Software Development Consulting</div>
  <nav class="main-nav">
    <a class="is-active" style="left:379px">HOME</a>
    <a style="left:442px">ABOUT US</a>
    <a style="left:515px">JOB POSTINGS</a>
    <a style="left:604px">CONTACT</a>
  </nav>
</header>

<section class="hero">
  <div class="hero-backdrop" role="img" aria-label="Blurred warm-toned photo of a developer workspace"></div>
  <div class="hero-arrow" style="left:50px"><svg width="12" height="14" viewBox="0 0 12 14"><path d="M8 1 L3 7 L8 13" fill="none" stroke="#cfcfcf" stroke-width="1.3"/></svg></div>
  <div class="hero-arrow" style="left:609px"><svg width="12" height="14" viewBox="0 0 12 14"><path d="M4 1 L9 7 L4 13" fill="none" stroke="#cfcfcf" stroke-width="1.3"/></svg></div>
  <h1 class="abs hero-title">DUIS AUTEM VEL EUM</h1>
  <ul class="hero-points">
    <li style="top:124px"><svg width="12" height="12" viewBox="0 0 12 12"><circle cx="6" cy="6" r="5" fill="none" stroke="#fff" stroke-width="1.3"/><path d="M3.2 6 L5.6 8.4 L11 2" fill="none" stroke="#fff" stroke-width="1.6"/></svg>Nam liber tempor cum soluta nobis</li>
    <li style="top:149px"><svg width="12" height="12" viewBox="0 0 12 12"><circle cx="6" cy="6" r="5" fill="none" stroke="#fff" stroke-width="1.3"/><path d="M3.2 6 L5.6 8.4 L11 2" fill="none" stroke="#fff" stroke-width="1.6"/></svg>eleifend option congue nihil imperdiet</li>
    <li style="top:174px"><svg width="12" height="12" viewBox="0 0 12 12"><circle cx="6" cy="6" r="5" fill="none" stroke="#fff" stroke-width="1.3"/><path d="M3.2 6 L5.6 8.4 L11 2" fill="none" stroke="#fff" stroke-width="1.6"/></svg>Typi non habent claritatem insitam</li>
  </ul>
  <div class="abs hero-device">
    <div class="hero-device-screen" role="img" aria-label="Tablet screen showing blue source code"></div>
  </div>
</section>

<h2 class="abs intro-heading">VI OPTIMERER DIN ONLINE DNA</h2>
<p class="abs intro-text">Vivamus sagittis lacus vel augue laoreet rutrum faucibus dolor auctor. Aenean lacinia bibendum nulla sed consectetur. Because we think it's time for a new excite! Are you ready for an adventure to remember for a lifetime? Accusantium quaim, ultricies eget tempor id, aliquam eget nibh et. Maecen aliquairis</p>

<div class="service" style="left:80px">
  <svg class="service-icon" width="47" height="47" viewBox="0 0 47 47"><circle cx="23.5" cy="23.5" r="23.5" fill="var(--brand)"/><g fill="none" stroke="#fff" stroke-width="1.6"><circle cx="23.5" cy="23.5" r="4"/><path d="M23.5 12 v3 M23.5 32 v3 M12 23.5 h3 M32 23.5 h3 M15.4 15.4 l2.1 2.1 M29.5 29.5 l2.1 2.1 M15.4 31.6 l2.1 -2.1 M29.5 17.5 l2.1 -2.1"/><circle cx="23.5" cy="23.5" r="8.5"/></g></svg>
  <div class="service-title">Software Development</div>
  <p class="service-text">Lorem ipsum dolor sit amet adipis msan. Morbi ut elit utipsum tristiqua Pellentesque habitant morbi.</p>
</div>
<div class="service" style="left:261px">
  <svg class="service-icon" width="47" height="47" viewBox="0 0 47 47"><circle cx="23.5" cy="23.5" r="23.5" fill="var(--brand)"/><path d="M23.5 11 L35 17 L35 30 L23.5 36 L12 30 L12 17 Z" fill="#fff"/><path d="M12 17 L23.5 23 L35 17 M23.5 23 V36" fill="none" stroke="var(--brand)" stroke-width="1.6"/></svg>
  <div class="service-title">Project Management</div>
  <p class="service-text">Lorem ipsum dolor sit amet adipis msan. Morbi ut elit utipsum tristiqua Pellentesque habitant morbi.</p>
</div>
<div class="service" style="left:445px">
  <svg class="service-icon" width="47" height="47" viewBox="0 0 47 47"><circle cx="23.5" cy="23.5" r="23.5" fill="var(--brand)"/><path d="M23.5 10 a8.5 8.5 0 0 1 5 15.4 V29 h-10 v-3.6 A8.5 8.5 0 0 1 23.5 10 Z" fill="#fff"/><rect x="19" y="30.5" width="9" height="2" fill="#fff"/><rect x="19.8" y="33.5" width="7.4" height="2" fill="#fff"/><path d="M22.5 36.5 h2 l-1 1.4 z" fill="#fff"/></svg>
  <div class="service-title">Industry Services</div>
  <p class="service-text">Lorem ipsum dolor sit amet adipis msan. Morbi ut elit utipsum tristiqua Pellentesque habitant morbi.</p>
</div>

<h2 class="abs column-heading" style="left:75px">JOBS</h2>
<div class="abs jobs-subheading">WE ARE HIRING?</div>
<div class="job" style="top:687px">
  <svg width="11" height="11" viewBox="0 0 11 11"><circle cx="5.5" cy="5.5" r="5.5" fill="var(--link)"/><path d="M4.3 3 L6.8 5.5 L4.3 8" fill="none" stroke="#fff" stroke-width="1.3"/></svg>
  <div class="job-title">Mobile Game Developer</div>
  <div class="job-detail">Mobile game developer - HTML, CSS, JavaScript</div>
</div>
<div class="job" style="top:725px">
  <svg width="11" height="11" viewBox="0 0 11 11"><circle cx="5.5" cy="5.5" r="5.5" fill="var(--link)"/><path d="M4.3 3 L6.8 5.5 L4.3 8" fill="none" stroke="#fff" stroke-width="1.3"/></svg>
  <div class="job-title">Mobile Game Developer</div>
  <div class="job-detail">Mobile game developer - HTML, CSS, JavaScript</div>
</div>

<h2 class="abs column-heading" style="left:392px">NEWS</h2>
<ul class="news-list">
  <li style="top:661px">Duis autem vel eum iriure dolor in hendrerit in vulputate velit Typi non habent claritatem insitam; est usus legentis in iis facit eorum claritatem.</li>
  <li style="top:712px">Duis autem vel eum iriure dolor in hendrerit in vulputate velit Typi non habent claritatem insitam; est usus legentis in iis facit eorum claritatem.</li>
</ul>

<h2 class="abs contact-heading">CONTACT US</h2>
<div class="abs field-label" style="top:844px">Name</div>
<div class="field field-input" style="top:858px">Your Name</div>
<div class="abs field-label" style="top:906px">Email</div>
<div class="field field-input" style="top:921px">Email id</div>
<div class="abs field-label" style="top:974px">Message</div>
<div class="field field-message" style="top:987px">send your message</div>
<div class="abs send-button">SEND</div>

<div class="abs location-map" role="img" aria-label="Street map showing the office location"></div>

<div class="contact-info" style="left:415px; top:983px">
  <svg width="8" height="11" viewBox="0 0 8 11"><path d="M4 0 a4 4 0 0 1 4 4 c0 3 -4 7 -4 7 s-4 -4 -4 -7 a4 4 0 0 1 4 -4 z" fill="#444"/><circle cx="4" cy="4" r="1.5" fill="#fff"/></svg>
  48 Harrow Lane<br>&nbsp;Westbrook 20417<br>Northfield
</div>
<div class="contact-info" style="left:552px; top:983px">
  <svg width="11" height="8" viewBox="0 0 11 8" style="left:-20px"><rect x="0.5" y="0.5" width="10" height="7" fill="none" stroke="#444"/><path d="M0.5 0.5 L5.5 4.5 L10.5 0.5" fill="none" stroke="#444"/></svg>
  hello@keelstone.example
</div>
<div class="contact-info" style="left:552px; top:1010px">
  <svg width="9" height="9" viewBox="0 0 9 9" style="left:-19px"><path d="M1.5 0 L3.3 0 L3.8 2.4 L2.6 3.3 C3.2 4.6 4.4 5.8 5.7 6.4 L6.6 5.2 L9 5.7 L9 7.5 C9 8.3 8.3 9 7.5 9 C3.4 9 0 5.6 0 1.5 C0 0.7 0.7 0 1.5 0 Z" fill="#444"/></svg>
  55 410 2276
</div>

<footer class="site-footer">
  <div class="abs footer-links">Terms and Conditions | Privacy Promise | FAQ's | Contact Us</div>
  <div class="abs footer-copy">Copyright © 2013. All Rights Reserved.</div>
  <span class="social" style="left:527px; background:#3b5598"></span>
  <span class="social" style="left:555px; background:#2aa3d8"></span>
  <span class="social" style="left:583px; background:#f07d1d"></span>
  <span class="social" style="left:612px; background:#d8262a"></span>
</footer>

</body>
</html>
```